Sunmeadow Home Care Business Card

We are a home care company customizing in personal care services. Our personal care service is different because our mission is to provide the most effective care while enhancing quality of life. We strive to make everyday our client's best day. I would like a very classic and/or retro feel. I don't like clip art.

Target Market(s)

doctor's offices; potential clients

Industry/Entity Type

Business

Contact Information for Business Card

jdalton@sunmeadowhc.example(919) 480-15904000 Blue Ridge Road, Suite 101Raleigh, NC 27612www.SunmeadowHC.example

Requirements
Must have
• classic and/or retro feel. Very caring.
Should not have
• Clip art

```html
<!DOCTYPE html>
<html lang="en">
<head>
<meta charset="utf-8">
<title>Sunmeadow Home Care – Business Card</title>
<link rel="stylesheet" href="https://fonts.googleapis.com/css2?family=Arimo:wght@400&family=Tinos:wght@400&display=swap">
<style>
  :root {
    --page: #ece7df;
    --card-white: #ffffff;
    --brown-dark: #3b2417;
    --tan: #8b7148;
    --gold: #9c8152;
    --gold-soft: #b39a6c;
    --ink-light: #f4efe6;
    --brand-blue: #2a9fd8;
  }
  * { margin: 0; padding: 0; box-sizing: border-box; }
  html, body { width: 1200px; height: 702px; overflow: hidden; }
  body {
    background: var(--page);
    position: relative;
    font-family: "Arimo", Arial, sans-serif;
  }
  .card {
    position: absolute;
    top: 196px;
    width: 520px;
    height: 310px;
    overflow: hidden;
    box-shadow: 0 6px 18px rgba(0,0,0,0.25);
  }
  .card--front { left: 50px; background: var(--card-white); }
  .card--back { left: 630px; background: var(--tan); }

  .front-shape, .stripes { position: absolute; inset: 0; }

  .flourish {
    position: absolute;
    background: var(--gold);
  }
  .flourish--corner {
    top: 28px; right: 0;
    width: 150px; height: 92px;
    border-radius: 70px 0 0 70px;
    opacity: 0.55;
  }
  .flourish--side {
    top: 128px; left: 0;
    width: 118px; height: 150px;
    border-radius: 0 80px 80px 0;
    background: var(--gold-soft);
    opacity: 0.5;
  }

  .brand-name {
    position: absolute;
    top: 62px; left: 46px;
    font-size: 30px;
    line-height: 1.1;
    color: var(--brand-blue);
    font-weight: 400;
  }

  .contact {
    position: absolute;
    top: 184px; left: 196px;
    color: var(--ink-light);
    font-style: normal;
    font-size: 14.5px;
    line-height: 1.5;
  }
  .contact__email { font-family: "Tinos", "Times New Roman", serif; font-size: 13.5px; }
  .contact__web { font-family: "Tinos", "Times New Roman", serif; font-size: 14.5px; }

  .back-mark {
    position: absolute;
    left: 0; right: 0;
    top: 128px;
    display: flex;
    align-items: center;
    justify-content: center;
    gap: 14px;
  }
  .back-mark__square {
    width: 34px; height: 34px;
    background: var(--card-white);
  }
  .back-mark__name {
    font-size: 26px;
    color: var(--card-white);
    font-weight: 400;
    line-height: 1;
  }
</style>
</head>
<body>

  <section class="card card--front" aria-label="Business card front">
    <svg class="front-shape" viewBox="0 0 520 310" width="520" height="310" aria-hidden="true">
      <path d="M0 120 C 70 150, 150 185, 300 190 L 520 190 L 520 310 L 0 310 Z" fill="var(--brown-dark)"/>
    </svg>
    <div class="flourish flourish--corner" role="img" aria-label="Gold floral flourish in the top corner"></div>
    <div class="flourish flourish--side" role="img" aria-label="Gold floral flourish on the left edge"></div>

    <h1 class="brand-name">Sunmeadow<br>Home Care, Inc.</h1>

    <address class="contact">
      <div class="contact__email">jdalton@sunmeadowhc.example</div>
      <div class="contact__phone">(555) 302-7741</div>
      <div class="contact__street">2700 Copper Finch Lane, Suite 101</div>
      <div class="contact__city">Linden Falls, NC 27500</div>
      <div class="contact__web">www.SunmeadowHC.example</div>
    </address>
  </section>

  <section class="card card--back" aria-label="Business card back">
    <svg class="stripes" viewBox="0 0 520 310" width="520" height="310" aria-hidden="true">
      <rect x="0" y="30" width="520" height="16" fill="var(--brown-dark)"/>
      <rect x="0" y="52" width="520" height="2" fill="var(--card-white)"/>
      <rect x="0" y="70" width="520" height="16" fill="var(--brown-dark)"/>
      <rect x="0" y="104" width="520" height="2" fill="var(--card-white)"/>
      <rect x="0" y="196" width="520" height="16" fill="var(--brown-dark)"/>
      <rect x="0" y="222" width="520" height="14" fill="var(--brown-dark)"/>
      <rect x="0" y="244" width="520" height="2" fill="var(--card-white)"/>
      <rect x="0" y="262" width="520" height="14" fill="var(--brown-dark)"/>
      <rect x="0" y="284" width="520" height="2" fill="var(--card-white)"/>
      <rect x="0" y="298" width="520" height="12" fill="var(--brown-dark)"/>
    </svg>
    <div class="back-mark">
      <span class="back-mark__square" aria-hidden="true"></span>
      <p class="back-mark__name">Sunmeadow Home Care</p>
    </div>
  </section>

</body>
</html>
```